The Gallowmere Notes Theatre Production Poster

We're after a poster for a theatre production based on R.T Ambrey's book, The Gallowmere Notes.
This play follows the story of a senior demon teaching a student demon how to tempt humankind. The tone of the play is light and formal with dark undertones and moments of levity. Hell is set in a university. I am wanting an eye-catching poster. Something subtle and NOT in the theme of 'horror'. I am open to different creative ideas, but I like the idea of a book being involved and maybe some shadow loosely representing a demon reading the book. Another idea could be a shadow hovering over a silhouetted human.
Other details that the poster must include:
- The Name of the Show: The Gallowmere Notes
- Time of the shows: 7:30 pm
- Dates of the show: Saturday 8th and 15th of October 2022
- Location: Brindlecombe Civic Theatre
- Organisation: Lanterngate Theatre Productions
- ticket price: $38
- bookings made at: https://app.seatvane-example.org.au/LanterngateTheatreProductions/Gallowmere
Target Market(s)
university Students
Industry/Entity Type
Theatre
Look and feel
Each slider illustrates characteristics of the customer's brand and the style your logo design should communicate.

```html
<!DOCTYPE html>
<html lang="en">
<head>
<meta charset="utf-8">
<title>The Gallowmere Notes – Poster</title>
<link href="https://fonts.googleapis.com/css2?family=Encode+Sans+Condensed:wght@400;500;600&family=Leckerli+One&display=swap" rel="stylesheet">
<style>
  :root {
    --page-bg: #ececee;
    --purple-light: #a560b4;
    --purple-mid: #7f3596;
    --purple-deep: #5e2276;
    --gold: #f6b126;
    --title-red: #d8383a;
    --label-bg: #333033;
    --label-text: #ffffff;
    --star: #f7c22b;
  }
  * { margin: 0; padding: 0; box-sizing: border-box; }
  html, body { width: 1200px; height: 960px; overflow: hidden; background: var(--page-bg); }
  .canvas { position: relative; width: 1200px; height: 960px; }

  .poster {
    position: absolute; left: 275px; top: 20px; width: 650px; height: 920px;
    overflow: hidden; border-radius: 3px;
    background: linear-gradient(180deg, var(--purple-light) 0%, var(--purple-mid) 50%, var(--purple-deep) 100%);
    font-family: "Encode Sans Condensed", "Arial Narrow", sans-serif;
  }
  .silhouettes {
    position: absolute; inset: 0;
    background:
      radial-gradient(ellipse 150px 420px at 520px 330px, rgba(201,80,124,0.95) 0%, rgba(201,80,124,0.75) 55%, rgba(201,80,124,0) 100%),
      radial-gradient(ellipse 170px 520px at 170px 520px, rgba(80,20,100,0.45) 0%, rgba(80,20,100,0) 100%),
      radial-gradient(ellipse 120px 420px at 330px 640px, rgba(90,30,120,0.45) 0%, rgba(90,30,120,0) 100%);
  }

  .tagline {
    position: absolute; top: 148px; left: 0; width: 100%;
    display: flex; justify-content: center; align-items: center; gap: 8px;
    color: var(--label-text); font-weight: 600; font-size: 23px; letter-spacing: 0.3px;
  }
  .stars { display: flex; gap: 2px; }
  .stars svg { width: 28px; height: 28px; fill: var(--star); }

  .presenter {
    position: absolute; top: 203px; right: 18px;
    display: flex; flex-direction: column; align-items: center;
    color: var(--label-text); font-weight: 500; font-size: 26px; line-height: 1;
  }
  .presenter span { background: var(--label-bg); padding: 4px 8px 5px; }

  .show-title {
    position: absolute; top: 188px; left: 40px; width: 570px;
    font-family: "Leckerli One", cursive; font-weight: 400; color: var(--gold);
    text-shadow:
      2px 0 0 var(--title-red), -2px 0 0 var(--title-red),
      0 2px 0 var(--title-red), 0 -2px 0 var(--title-red),
      1.5px 1.5px 0 var(--title-red), -1.5px -1.5px 0 var(--title-red),
      1.5px -1.5px 0 var(--title-red), -1.5px 1.5px 0 var(--title-red),
      4px 6px 8px rgba(40,0,40,0.5);
    line-height: 0.95;
  }
  .show-title .line { display: block; }
  .show-title .the { font-size: 100px; margin-left: 105px; }
  .show-title .main { font-size: 104px; letter-spacing: -2px; }
  .show-title .notes { font-size: 112px; margin-left: 150px; }

  .details {
    position: absolute; top: 594px; left: 0; width: 100%;
    display: flex; flex-direction: column; align-items: center; gap: 6px;
    color: var(--label-text); line-height: 1;
  }
  .details span { background: var(--label-bg); white-space: nowrap; }
  .dates { font-size: 42px; font-weight: 500; padding: 9px 12px 10px; }
  .venue { font-size: 34px; font-weight: 500; padding: 6px 10px 7px; }
  .tickets { font-size: 23px; font-weight: 500; padding: 6px 8px 6px; }

  .bookings {
    position: absolute; top: 827px; left: 50%; transform: translateX(-50%);
    white-space: nowrap; background: var(--label-bg); color: var(--label-text);
    font-size: 14px; letter-spacing: 0.2px; padding: 6px 12px 7px;
  }
</style>
</head>
<body>
<div class="canvas">
  <article class="poster">
    <div class="silhouettes" role="img" aria-label="Soft shadow silhouettes of a tall horned demon figure in pink looming over two cloaked human figures"></div>

    <p class="tagline">
      <span class="stars" aria-hidden="true">
        <svg viewBox="0 0 24 24"><path d="M12 1.5l3.1 6.6 7.2.9-5.3 5 1.4 7.1L12 17.6l-6.4 3.5 1.4-7.1-5.3-5 7.2-.9z"/></svg>
        <svg viewBox="0 0 24 24"><path d="M12 1.5l3.1 6.6 7.2.9-5.3 5 1.4 7.1L12 17.6l-6.4 3.5 1.4-7.1-5.3-5 7.2-.9z"/></svg>
        <svg viewBox="0 0 24 24"><path d="M12 1.5l3.1 6.6 7.2.9-5.3 5 1.4 7.1L12 17.6l-6.4 3.5 1.4-7.1-5.3-5 7.2-.9z"/></svg>
      </span>
      BASED ON R.T AMBREY’S NOVEL
      <span class="stars" aria-hidden="true">
        <svg viewBox="0 0 24 24"><path d="M12 1.5l3.1 6.6 7.2.9-5.3 5 1.4 7.1L12 17.6l-6.4 3.5 1.4-7.1-5.3-5 7.2-.9z"/></svg>
        <svg viewBox="0 0 24 24"><path d="M12 1.5l3.1 6.6 7.2.9-5.3 5 1.4 7.1L12 17.6l-6.4 3.5 1.4-7.1-5.3-5 7.2-.9z"/></svg>
        <svg viewBox="0 0 24 24"><path d="M12 1.5l3.1 6.6 7.2.9-5.3 5 1.4 7.1L12 17.6l-6.4 3.5 1.4-7.1-5.3-5 7.2-.9z"/></svg>
      </span>
    </p>

    <p class="presenter">
      <span>LANTERNGATE THEATRE</span>
      <span>PRODUCTIONS PRESENTS</span>
    </p>

    <h1 class="show-title">
      <span class="line the">The</span>
      <span class="line main">Gallowmere</span>
      <span class="line notes">Notes</span>
    </h1>

    <div class="details">
      <span class="dates">Saturday 8 &amp; 15 October 2022</span>
      <span class="venue">Brindlecombe Civic Theatre</span>
      <span class="tickets">Tickets $38.00, show starts 7.30pm</span>
    </div>

    <p class="bookings">Bookings made at: https://app.seatvane-example.org.au/LanterngateTheatreProductions/Gallowmere</p>
  </article>
</div>
</body>
</html>
```